Financial Statements templates

We are a accounting and bookkeeping firms, we are trying to change the presentation of the clients' financial statements in a more professional and interesting way using graphics and PowerPoint skills, each client should feel that his/her FS are unique and developed for him/her, first will start with the normal financial statements (Balance sheet, income statement and cash flow) and then with the financial highlights, ratios and facts where we can use the charts and graphics

Reason: More time for more ideas

Reason: I want to give more time to the participants and i did not quite liked the submitted designs so far

Target Market(s)

different industry

Industry/Entity Type

Accounting

Colors

Designer to choose colors to be used in the design.

Requirements
Must have
• We would like to have a template where we can use with different clients as we need to only update their figures and upload their logos along with our below logo i.e. lindomark+ as a maker/prepared by. each client should feel that their Financial Statement is customized for them.
• Should also include charts and graphics,

```html
<!DOCTYPE html>
<html lang="en">
<head>
<meta charset="utf-8">
<title>Financial Statements Template</title>
<link rel="stylesheet" href="https://fonts.googleapis.com/css2?family=Libre+Franklin:wght@400;600;700&family=Roboto:wght@400;700&display=swap">
<style>
:root{
  --navy:#14265a;
  --green:#6bbd3a;
  --green-mid:#4f9a2b;
  --green-dark:#2f6b1e;
  --green-pale:#b8e09a;
  --blue:#2f6fce;
  --bar:#3d3d40;
  --ink:#3b3b3b;
  --muted:#777;
  --rule:#dcdcdc;
}
*{box-sizing:border-box;margin:0;padding:0}
html,body{width:1200px;height:2961px;overflow:hidden;background:#fff}
body{position:relative;font-family:"Roboto",Arial,sans-serif;color:var(--ink)}
.slide{position:absolute;width:542px;height:304px;background:#fff;box-shadow:0 1px 4px rgba(0,0,0,.22)}
.col-l{left:44px}.col-r{left:634px}
.bar-top{position:absolute;left:0;top:0;width:100%;height:6px;background:var(--bar)}
.bar-top::before{content:"";position:absolute;left:40px;top:0;width:146px;height:6px;background:var(--navy);border-left:3px solid #fff;border-right:3px solid #fff}
.bar-bottom{position:absolute;left:0;bottom:0;width:100%;height:6px;background:var(--bar)}
.bar-bottom::before{content:"";position:absolute;left:358px;bottom:0;width:146px;height:9px;background:var(--green);border-left:3px solid #fff;border-right:3px solid #fff}
.page-no{position:absolute;right:12px;bottom:10px;font-size:5px;color:#999}
.title{position:absolute;left:34px;top:22px;font-family:"Libre Franklin",Arial,sans-serif;font-weight:700;font-size:12.5px;color:var(--navy);letter-spacing:.1px}
.cover-title{position:absolute;left:0;width:100%;top:70px;text-align:center;font-family:"Libre Franklin",Arial,sans-serif;font-weight:700;font-size:29px;line-height:1.12;color:var(--navy)}
.cover-lead{position:absolute;left:106px;width:330px;top:150px;text-align:center;font-size:9px;line-height:1.35;color:#555}
.panel{position:absolute;top:6px;bottom:6px}
.panel-green{left:358px;width:146px;background:var(--green)}
.panel-navy{left:40px;width:146px;background:var(--navy)}
.tbl{position:absolute;border-collapse:collapse;font-size:6px;color:var(--ink)}
.tbl th{color:var(--green-mid);font-weight:400;text-align:center;padding:1px 3px 2px;border-bottom:1px solid var(--green);line-height:1.15}
.tbl th.lbl{text-align:left}
.tbl td{border-bottom:1px solid var(--rule);padding:3px 4px;text-align:center;line-height:1.15}
.tbl td.txt{text-align:left}
.tbl tr.total td{font-weight:700;color:#222;border-bottom:none}
.tbl tr.first td{border-top:1px solid var(--green)}
.bullets{position:absolute;list-style:none;font-size:6px;line-height:1.35;color:#666}
.bullets li{position:relative;padding-left:9px;margin-bottom:11px}
.bullets li::before{content:"";position:absolute;left:0;top:2px;width:3px;height:3px;border-radius:50%;background:#888}
.note{position:absolute;font-size:6px;line-height:1.35;color:#666}
.caption{position:absolute;font-size:6.5px;line-height:1.35;color:#555}
.caption b,.subhead{font-family:"Libre Franklin",Arial,sans-serif;font-weight:700;color:#222;font-size:8px;display:block;margin-bottom:3px}
.subhead{position:absolute}
.chart{position:absolute;overflow:visible}
.chart text{font-family:"Roboto",Arial,sans-serif;fill:#777;font-size:5px}
.big-num{position:absolute;font-family:"Libre Franklin",Arial,sans-serif;font-size:21px;color:var(--green-mid);text-align:center;width:60px}
</style>
</head>
<body>

<!-- Row 1 -->
<section class="slide col-l" style="top:20px">
  <div class="bar-top"></div>
  <h1 class="cover-title">LOREM IPSUM DOLOR SIT<br>AMET CONSETETUR</h1>
  <p class="cover-lead">Lorem ipsum dolor sit amet, consetetur sadipscing elitr, sed diam nonumy eirmod tempor invidunt ut labore et dolore magna aliquyam erat, sed diam voluptua. At vero eos et accusam et justo duo dolores et ea rebum. Stet clita kasd gubergren, no sea takimata sanctus est</p>
  <div class="bar-bottom"></div>
</section>

<section class="slide col-r" style="top:20px">
  <div class="bar-top"></div>
  <h2 class="title">LOREM IPSUM DOLOR SIT AMET CONSETETUR</h2>
  <div class="bar-bottom"></div>
</section>

<!-- Row 2 -->
<section class="slide col-l" style="top:342px">
  <div class="bar-top"></div>
  <div class="panel panel-green"></div>
  <h2 class="title">LOREM IPSUM DOLOR SIT AMET</h2>
  <div class="bar-bottom"></div>
</section>

<section class="slide col-r" style="top:342px">
  <div class="bar-top"></div>
  <div class="panel panel-navy"></div>
  <h2 class="title" style="left:240px">LOREM IPSUM DOLOR SIT AMET</h2>
  <div class="bar-bottom"></div>
</section>

<!-- Row 3 -->
<section class="slide col-l" style="top:664px">
  <div class="bar-top"></div>
  <h2 class="title">LOREM IPSUM DOLOR SIT AMET CONSETETUR</h2>
  <table class="tbl" style="left:34px;top:62px;width:474px">
    <tr><th class="lbl"></th><th class="lbl"></th><th>Lorem<br>ipsum</th><th>Lorem<br>ipsum</th><th>Lorem<br>ipsum</th><th>Lorem<br>ipsum</th><th>Lorem<br>ipsum</th></tr>
    <tr><td class="txt">Lorem ipsum dolor sit amet consetetur sadipscing elitr</td><td class="txt">Lorem ipsum dolor</td><td>11</td><td>12</td><td>13</td><td>14</td><td>15</td></tr>
    <tr><td class="txt">Lorem ipsum dolor sit amet consetetur sadipscing elitr</td><td class="txt">Lorem ipsum dolor</td><td>56</td><td>60</td><td>64</td><td>68</td><td>72</td></tr>
    <tr><td class="txt">Lorem ipsum dolor sit amet consetetur sadipscing elitr</td><td class="txt">Lorem ipsum dolor</td><td>21</td><td>22</td><td>23</td><td>24</td><td>25</td></tr>
    <tr><td class="txt">Lorem ipsum dolor sit amet consetetur sadipscing elitr</td><td class="txt">Lorem ipsum dolor</td><td>14</td><td>14</td><td>15</td><td>16</td><td>16</td></tr>
    <tr class="total"><td class="txt">Lorem ipsum dolor sit amet consetetur sadipscing elitr</td><td class="txt">Lorem ipsum dolor</td><td>102</td><td>108</td><td>115</td><td>122</td><td>128</td></tr>
    <tr><td class="txt">Lorem ipsum dolor sit amet consetetur sadipscing elitr</td><td class="txt">Lorem ipsum dolor</td><td>11</td><td>12</td><td>13</td><td>14</td><td>15</td></tr>
    <tr><td class="txt">Lorem ipsum dolor sit amet consetetur sadipscing elitr</td><td class="txt">Lorem ipsum dolor</td><td>56</td><td>60</td><td>64</td><td>68</td><td>72</td></tr>
    <tr><td class="txt">Lorem ipsum dolor sit amet consetetur sadipscing elitr</td><td class="txt">Lorem ipsum dolor</td><td>21</td><td>22</td><td>23</td><td>24</td><td>25</td></tr>
    <tr><td class="txt">Lorem ipsum dolor sit amet consetetur sadipscing elitr</td><td class="txt">Lorem ipsum dolor</td><td>11</td><td>12</td><td>13</td><td>14</td><td>15</td></tr>
    <tr class="total"><td class="txt">Lorem ipsum dolor sit amet consetetur sadipscing elitr</td><td class="txt">Lorem ipsum dolor</td><td>99</td><td>106</td><td>113</td><td>120</td><td>127</td></tr>
  </table>
  <span class="page-no">5</span>
  <div class="bar-bottom"></div>
</section>

<section class="slide col-r" style="top:664px">
  <div class="bar-top"></div>
  <h2 class="title">LOREM IPSUM DOLOR SIT AMET CONSETETUR</h2>
  <table class="tbl" style="left:34px;top:72px;width:474px">
    <tr><th class="lbl"></th><th>Lorem<br>ipsum</th><th>Lorem<br>ipsum</th><th>Lorem<br>ipsum</th><th>Lorem<br>ipsum</th><th>Lorem<br>ipsum</th><th>Lorem<br>ipsum</th><th>Lorem<br>ipsum</th><th>Lorem<br>ipsum</th></tr>
    <tr><td class="txt">Lorem ipsum dolor sit amet, consetetur<br>sadipscing elitr, sed diam nonumy eirmod</td><td>11</td><td>12</td><td>13</td><td>14</td><td>15</td><td>16</td><td>17</td><td>18</td></tr>
    <tr><td class="txt">Lorem ipsum dolor sit amet, consetetur<br>sadipscing elitr, sed diam nonumy eirmod</td><td>56</td><td>60</td><td>64</td><td>68</td><td>72</td><td>76</td><td>80</td><td>84</td></tr>
    <tr><td class="txt">Lorem ipsum dolor sit amet, consetetur<br>sadipscing elitr, sed diam nonumy eirmod</td><td>21</td><td>22</td><td>23</td><td>24</td><td>25</td><td>26</td><td>27</td><td>28</td></tr>
    <tr><td class="txt">Lorem ipsum dolor sit amet, consetetur<br>sadipscing elitr, sed diam nonumy eirmod</td><td>14</td><td>14</td><td>15</td><td>15</td><td>16</td><td>17</td><td>17</td><td>18</td></tr>
    <tr><td class="txt">Lorem ipsum dolor sit amet, consetetur<br>sadipscing elitr, sed diam nonumy eirmod</td><td>4</td><td>4</td><td>4</td><td>5</td><td>5</td><td>5</td><td>5</td><td>6</td></tr>
    <tr class="total"><td class="txt">Lorem ipsum dolor sit amet, consetetur</td><td>106</td><td>112</td><td>119</td><td>126</td><td>133</td><td>140</td><td>146</td><td>154</td></tr>
  </table>
  <span class="page-no">6</span>
  <div class="bar-bottom"></div>
</section>

<!-- Row 4 -->
<section class="slide col-l" style="top:986px">
  <div class="bar-top"></div>
  <h2 class="title">LOREM IPSUM DOLOR SIT AMET CONSETETUR</h2>
  <table class="tbl" style="left:34px;top:62px;width:300px">
    <tr><th class="lbl"></th><th>Lorem<br>ipsum</th><th>Lorem<br>ipsum</th><th>Lorem<br>ipsum</th><th>Lorem<br>ipsum</th></tr>
    <tr class="first"><td class="txt">Lorem ipsum dolor sit amet,<br>consetetur sadipscing elitr</td><td>11</td><td>12</td><td>13</td><td>14</td></tr>
    <tr><td class="txt">Lorem ipsum dolor sit amet,<br>consetetur sadipscing elitr</td><td>56</td><td>60</td><td>64</td><td>68</td></tr>
    <tr><td class="txt">Lorem ipsum dolor sit amet,<br>consetetur sadipscing elitr</td><td>21</td><td>22</td><td>23</td><td>24</td></tr>
    <tr><td class="txt">Lorem ipsum dolor sit amet,<br>consetetur sadipscing elitr</td><td>14</td><td>14</td><td>15</td><td>15</td></tr>
    <tr><td class="txt">Lorem ipsum dolor sit amet,<br>consetetur sadipscing elitr</td><td>4</td><td>4</td><td>4</td><td>5</td></tr>
    <tr class="total"><td class="txt">Lorem ipsum dolor sit amet, consetetur<br>sadipscing elitr</td><td>106</td><td>112</td><td>119</td><td>126</td></tr>
  </table>
  <ul class="bullets" style="left:356px;top:90px;width:150px">
    <li>Lorem ipsum dolor sit amet, consetetur sadipscing elitr, sed diam nonumy eirmod tempor invidunt ut labore et dolore magna aliquyam erat, sed diam voluptua. At vero eos et accusam</li>
    <li>Lorem ipsum dolor sit amet, consetetur sadipscing elitr, sed diam nonumy eirmod tempor invidunt ut labore et dolore magna aliquyam erat. At vero eos et accusam</li>
  </ul>
  <span class="page-no">7</span>
  <div class="bar-bottom"></div>
</section>

<section class="slide col-r" style="top:986px">
  <div class="bar-top"></div>
  <h2 class="title">LOREM IPSUM DOLOR SIT AMET CONSETETUR</h2>
  <table class="tbl" style="left:34px;top:62px;width:474px">
    <tr><th class="lbl"></th><th>Lorem<br>ipsum</th><th>Lorem<br>ipsum</th><th>Lorem<br>ipsum</th><th class="lbl">Lorem ipsum dolor sit amet, consetetur sadipscing elitr</th></tr>
    <tr class="first"><td class="txt">Lorem ipsum dolor sit amet, consetetur<br>sadipscing elitr</td><td>11</td><td>12</td><td>13</td><td class="txt">Lorem ipsum dolor sit amet, consetetur sadipscing elitr</td></tr>
    <tr><td class="txt">Lorem ipsum dolor sit amet, consetetur<br>sadipscing elitr</td><td>56</td><td>60</td><td>64</td><td class="txt">Lorem ipsum dolor sit amet, consetetur sadipscing elitr</td></tr>
    <tr><td class="txt">Lorem ipsum dolor sit amet, consetetur<br>sadipscing elitr</td><td>21</td><td>22</td><td>23</td><td class="txt">Lorem ipsum dolor sit amet, consetetur sadipscing elitr</td></tr>
    <tr><td class="txt">Lorem ipsum dolor sit amet, consetetur<br>sadipscing elitr</td><td>14</td><td>14</td><td>15</td><td class="txt">Lorem ipsum dolor sit amet, consetetur sadipscing elitr</td></tr>
    <tr><td class="txt">Lorem ipsum dolor sit amet, consetetur<br>sadipscing elitr</td><td>4</td><td>4</td><td>4</td><td class="txt">Lorem ipsum dolor sit amet, consetetur sadipscing elitr</td></tr>
    <tr class="total"><td class="txt">Lorem ipsum dolor sit amet, consetetur<br>sadipscing elitr</td><td>106</td><td>112</td><td>119</td><td class="txt">Lorem ipsum dolor sit amet, consetetur sadipscing elitr</td></tr>
  </table>
  <span class="page-no">8</span>
  <div class="bar-bottom"></div>
</section>

<!-- Row 5 -->
<section class="slide col-l" style="top:1308px">
  <div class="bar-top"></div>
  <h2 class="title">LOREM IPSUM DOLOR SIT AMET CONSETETUR</h2>
  <table class="tbl" style="left:34px;top:56px;width:224px">
    <tr><th class="lbl"></th><th>Lorem<br>ipsum</th><th>Lorem<br>ipsum</th><th>Lorem<br>ipsum</th><th>Lorem<br>ipsum</th></tr>
    <tr class="first"><td class="txt">Lorem ipsum dolor sit<br>amet, consetetur</td><td>11</td><td>12</td><td>13</td><td>14</td></tr>
    <tr><td class="txt">Lorem ipsum dolor sit<br>amet, consetetur</td><td>56</td><td>60</td><td>64</td><td>68</td></tr>
    <tr><td class="txt">Lorem ipsum dolor sit<br>amet, consetetur</td><td>21</td><td>22</td><td>23</td><td>24</td></tr>
    <tr><td class="txt">Lorem ipsum dolor sit<br>amet, consetetur</td><td>14</td><td>14</td><td>15</td><td>15</td></tr>
    <tr><td class="txt">Lorem ipsum dolor sit<br>amet, consetetur</td><td>4</td><td>4</td><td>4</td><td>4</td></tr>
    <tr class="total"><td class="txt">Lorem ipsum dolor sit<br>amet, consetetur</td><td>106</td><td>112</td><td>119</td><td>126</td></tr>
  </table>
  <table class="tbl" style="left:284px;top:56px;width:224px">
    <tr><th class="lbl"></th><th>Lorem<br>ipsum</th><th>Lorem<br>ipsum</th><th>Lorem<br>ipsum</th><th>Lorem<br>ipsum</th></tr>
    <tr class="first"><td class="txt">Lorem ipsum dolor sit<br>amet, consetetur</td><td>11</td><td>12</td><td>13</td><td>14</td></tr>
    <tr><td class="txt">Lorem ipsum dolor sit<br>amet, consetetur</td><td>56</td><td>60</td><td>64</td><td>68</td></tr>
    <tr><td class="txt">Lorem ipsum dolor sit<br>amet, consetetur</td><td>21</td><td>22</td><td>23</td><td>24</td></tr>
    <tr><td class="txt">Lorem ipsum dolor sit<br>amet, consetetur</td><td>14</td><td>14</td><td>15</td><td>15</td></tr>
    <tr><td class="txt">Lorem ipsum dolor sit<br>amet, consetetur</td><td>4</td><td>4</td><td>4</td><td>4</td></tr>
    <tr class="total"><td class="txt">Lorem ipsum dolor sit<br>amet, consetetur</td><td>106</td><td>112</td><td>119</td><td>126</td></tr>
  </table>
  <p class="note" style="left:34px;top:244px;width:224px">Lorem ipsum dolor sit amet, consetetur sadipscing elitr, sed diam nonumy eirmod tempor invidunt ut labore et dolore magna aliquyam erat, sed diam voluptua. At vero eos et accusam</p>
  <p class="note" style="left:284px;top:244px;width:224px">Lorem ipsum dolor sit amet, consetetur sadipscing elitr, sed diam nonumy eirmod tempor invidunt ut labore et dolore magna aliquyam erat, sed diam voluptua. At vero eos et accusam</p>
  <span class="page-no">9</span>
  <div class="bar-bottom"></div>
</section>

<section class="slide col-r" style="top:1308px">
  <div class="bar-top"></div>
  <h2 class="title">LOREM IPSUM DOLOR SIT AMET CONSETETUR</h2>
  <table class="tbl" style="left:34px;top:56px;width:300px">
    <tr><th class="lbl"></th><th>Lorem<br>ipsum</th><th>Lorem<br>ipsum</th><th>±</th><th>Lorem<br>ipsum</th><th>Lorem<br>ipsum</th><th>±</th></tr>
    <tr class="first"><td class="txt">Lorem ipsum dolor sit<br>amet, consetetur</td><td>12</td><td>14</td><td>+2</td><td>33</td><td>35</td><td>+2</td></tr>
    <tr><td class="txt">Lorem ipsum dolor sit<br>amet, consetetur</td><td>11</td><td>9</td><td>-2</td><td>95</td><td>96</td><td>+1</td></tr>
    <tr><td class="txt">Lorem ipsum dolor sit<br>amet, consetetur</td><td>34</td><td>27</td><td>-7</td><td>88</td><td>90</td><td>+2</td></tr>
    <tr><td class="txt">Lorem ipsum dolor sit<br>amet, consetetur</td><td>11</td><td>12</td><td>+1</td><td>44</td><td>46</td><td>+2</td></tr>
    <tr class="total"><td class="txt">Total</td><td>67</td><td>62</td><td>-6</td><td>260</td><td>267</td><td>+7</td></tr>
    <tr><td class="txt">Lorem ipsum dolor sit<br>amet, consetetur</td><td>8</td><td>12</td><td>+4</td><td>38</td><td>36</td><td>-2</td></tr>
    <tr><td class="txt">Lorem ipsum dolor sit<br>amet, consetetur</td><td>6</td><td>10</td><td>+4</td><td>40</td><td>42</td><td>+2</td></tr>
    <tr><td class="txt">Lorem ipsum dolor sit<br>amet, consetetur</td><td>7</td><td>9</td><td>+2</td><td>26</td><td>27</td><td>+1</td></tr>
    <tr><td class="txt">Lorem ipsum dolor sit<br>amet, consetetur</td><td>19</td><td>20</td><td>+1</td><td>70</td><td>71</td><td>+1</td></tr>
    <tr class="total"><td class="txt">Total</td><td>40</td><td>51</td><td>+11</td><td>174</td><td>176</td><td>+2</td></tr>
  </table>
  <ul class="bullets" style="left:356px;top:66px;width:150px">
    <li>Lorem ipsum dolor sit amet, consetetur sadipscing elitr, sed diam nonumy eirmod tempor invidunt ut labore et dolore magna aliquyam erat. At vero eos et accusam</li>
    <li>Lorem ipsum dolor sit amet, consetetur sadipscing elitr, sed diam nonumy eirmod tempor invidunt ut labore et dolore magna aliquyam erat. At vero eos et accusam</li>
    <li>Lorem ipsum dolor sit amet, consetetur sadipscing elitr, sed diam nonumy eirmod tempor invidunt ut labore et dolore magna aliquyam erat. At vero eos et accusam</li>
  </ul>
  <span class="page-no">10</span>
  <div class="bar-bottom"></div>
</section>

<!-- Row 6 -->
<section class="slide col-l" style="top:1630px">
  <div class="bar-top"></div>
  <h2 class="title">LOREM IPSUM DOLOR SIT AMET CONSETETUR</h2>
  <div class="caption" style="left:34px;top:58px;width:150px"><b>Lorem ipsum</b>Lorem ipsum dolor sit amet, consetetur sadipscing elitr, sed diam nonumy eirmod tempor invidunt</div>
  <table class="tbl" style="left:34px;top:112px;width:150px">
    <tr><th class="lbl"></th><th>Lorem<br>ipsum</th><th>Lorem<br>ipsum</th><th>Lorem<br>ipsum</th></tr>
    <tr class="first"><td class="txt">Lorem ipsum<br>dolor sit amet</td><td>11</td><td>12</td><td>13</td></tr>
    <tr><td class="txt">Lorem ipsum<br>dolor sit amet</td><td>56</td><td>60</td><td>64</td></tr>
    <tr><td class="txt">Lorem ipsum<br>dolor sit amet</td><td>21</td><td>22</td><td>23</td></tr>
    <tr><td class="txt">Lorem ipsum<br>dolor sit amet</td><td>14</td><td>14</td><td>15</td></tr>
    <tr><td class="txt">Lorem ipsum<br>dolor sit amet</td><td>4</td><td>4</td><td>4</td></tr>
    <tr class="total"><td class="txt">Lorem ipsum<br>dolor sit amet</td><td>106</td><td>112</td><td>119</td></tr>
  </table>
  <div class="caption" style="left:196px;top:58px;width:150px"><b>Lorem ipsum</b>Lorem ipsum dolor sit amet, consetetur sadipscing elitr, sed diam nonumy eirmod tempor invidunt</div>
  <table class="tbl" style="left:196px;top:112px;width:150px">
    <tr><th class="lbl"></th><th>Lorem<br>ipsum</th><th>Lorem<br>ipsum</th><th>Lorem<br>ipsum</th></tr>
    <tr class="first"><td class="txt">Lorem ipsum<br>dolor sit amet</td><td>11</td><td>12</td><td>13</td></tr>
    <tr><td class="txt">Lorem ipsum<br>dolor sit amet</td><td>56</td><td>60</td><td>64</td></tr>
    <tr><td class="txt">Lorem ipsum<br>dolor sit amet</td><td>21</td><td>22</td><td>23</td></tr>
    <tr><td class="txt">Lorem ipsum<br>dolor sit amet</td><td>14</td><td>14</td><td>15</td></tr>
    <tr><td class="txt">Lorem ipsum<br>dolor sit amet</td><td>4</td><td>4</td><td>4</td></tr>
    <tr class="total"><td class="txt">Lorem ipsum<br>dolor sit amet</td><td>106</td><td>112</td><td>119</td></tr>
  </table>
  <div class="caption" style="left:358px;top:58px;width:150px"><b>Lorem ipsum</b>Lorem ipsum dolor sit amet, consetetur sadipscing elitr, sed diam nonumy eirmod tempor invidunt</div>
  <table class="tbl" style="left:358px;top:112px;width:150px">
    <tr><th class="lbl"></th><th>Lorem<br>ipsum</th><th>Lorem<br>ipsum</th><th>Lorem<br>ipsum</th></tr>
    <tr class="first"><td class="txt">Lorem ipsum<br>dolor sit amet</td><td>11</td><td>12</td><td>13</td></tr>
    <tr><td class="txt">Lorem ipsum<br>dolor sit amet</td><td>56</td><td>60</td><td>64</td></tr>
    <tr><td class="txt">Lorem ipsum<br>dolor sit amet</td><td>21</td><td>22</td><td>23</td></tr>
    <tr><td class="txt">Lorem ipsum<br>dolor sit amet</td><td>14</td><td>14</td><td>15</td></tr>
    <tr><td class="txt">Lorem ipsum<br>dolor sit amet</td><td>4</td><td>4</td><td>4</td></tr>
    <tr class="total"><td class="txt">Lorem ipsum<br>dolor sit amet</td><td>106</td><td>112</td><td>119</td></tr>
  </table>
  <span class="page-no">11</span>
  <div class="bar-bottom"></div>
</section>

<section class="slide col-r" style="top:1630px">
  <div class="bar-top"></div>
  <h2 class="title">LOREM IPSUM DOLOR SIT AMET CONSETETUR</h2>
  <svg class="chart" style="left:20px;top:54px" width="320" height="150" viewBox="0 0 320 150">
    <g stroke="#e6e6e6" stroke-width=".6">
      <line x1="22" y1="130" x2="318" y2="130"/><line x1="22" y1="113" x2="318" y2="113"/><line x1="22" y1="96" x2="318" y2="96"/><line x1="22" y1="79" x2="318" y2="79"/><line x1="22" y1="62" x2="318" y2="62"/><line x1="22" y1="45" x2="318" y2="45"/><line x1="22" y1="28" x2="318" y2="28"/><line x1="22" y1="11" x2="318" y2="11"/>
    </g>
    <g text-anchor="end"><text x="18" y="132">0</text><text x="18" y="115">10</text><text x="18" y="98">20</text><text x="18" y="81">30</text><text x="18" y="64">40</text><text x="18" y="47">50</text><text x="18" y="30">60</text><text x="18" y="13">70</text></g>
    <g fill="var(--blue)">
      <rect x="32" y="99" width="11" height="31"/><rect x="66" y="86" width="11" height="44"/><rect x="100" y="81" width="11" height="49"/><rect x="134" y="74" width="11" height="56"/><rect x="168" y="69" width="11" height="61"/><rect x="202" y="65" width="11" height="65"/><rect x="236" y="59" width="11" height="71"/><rect x="270" y="69" width="11" height="61"/>
    </g>
    <g fill="var(--green)">
      <rect x="44" y="93" width="11" height="37"/><rect x="78" y="79" width="11" height="51"/><rect x="112" y="76" width="11" height="54"/><rect x="146" y="69" width="11" height="61"/><rect x="180" y="62" width="11" height="68"/><rect x="214" y="52" width="11" height="78"/><rect x="248" y="31" width="11" height="99"/><rect x="282" y="55" width="11" height="75"/>
    </g>
    <g text-anchor="middle"><text x="44" y="139">Text</text><text x="78" y="139">Text</text><text x="112" y="139">Text</text><text x="146" y="139">Text</text><text x="180" y="139">Text</text><text x="214" y="139">Text</text><text x="248" y="139">Text</text><text x="282" y="139">Text</text></g>
    <rect x="300" y="110" width="4" height="4" fill="var(--green)"/><text x="306" y="114">Text</text>
    <rect x="300" y="118" width="4" height="4" fill="var(--blue)"/><text x="306" y="122">Text</text>
  </svg>
  <div class="caption" style="left:34px;top:236px;width:260px"><b>Lorem ipsum</b>Lorem ipsum dolor sit amet, consetetur sadipscing elitr, sed diam nonumy eirmod tempor invidunt ut labore et dolore</div>
  <ul class="bullets" style="left:356px;top:66px;width:150px">
    <li>Lorem ipsum dolor sit amet, consetetur sadipscing elitr, sed diam nonumy eirmod tempor invidunt ut labore et dolore magna aliquyam erat, sed diam voluptua. At vero eos et accusam</li>
    <li>Lorem ipsum dolor sit amet, consetetur sadipscing elitr, sed diam nonumy eirmod tempor invidunt ut labore et dolore magna aliquyam erat, sed diam voluptua. At vero eos et accusam</li>
    <li>Lorem ipsum dolor sit amet, consetetur sadipscing elitr, sed diam nonumy eirmod tempor invidunt ut labore et dolore magna aliquyam erat, sed diam voluptua. At vero eos et accusam</li>
  </ul>
  <span class="page-no">12</span>
  <div class="bar-bottom"></div>
</section>

<!-- Row 7 -->
<section class="slide col-l" style="top:1952px">
  <div class="bar-top"></div>
  <h2 class="title">LOREM IPSUM DOLOR SIT AMET CONSETETUR</h2>
  <svg class="chart" style="left:30px;top:60px" width="290" height="110" viewBox="0 0 290 110">
    <line x1="10" y1="82" x2="235" y2="82" stroke="#e6e6e6" stroke-width=".6"/>
    <polyline fill="none" stroke="var(--navy)" stroke-width="1.6" points="16,26 46,22 76,30 106,20 136,28 166,22 196,26 226,14"/>
    <polyline fill="none" stroke="var(--green)" stroke-width="1.6" points="16,62 46,50 76,62 106,48 136,58 166,44 196,38 226,28"/>
    <g fill="#fff" stroke="var(--navy)" stroke-width="1.2"><circle cx="16" cy="26" r="2.6"/><circle cx="46" cy="22" r="2.6"/><circle cx="76" cy="30" r="2.6"/><circle cx="106" cy="20" r="2.6"/><circle cx="136" cy="28" r="2.6"/><circle cx="166" cy="22" r="2.6"/><circle cx="196" cy="26" r="2.6"/><circle cx="226" cy="14" r="2.6"/></g>
    <g fill="#fff" stroke="var(--green)" stroke-width="1.2"><circle cx="16" cy="62" r="2.6"/><circle cx="46" cy="50" r="2.6"/><circle cx="76" cy="62" r="2.6"/><circle cx="106" cy="48" r="2.6"/><circle cx="136" cy="58" r="2.6"/><circle cx="166" cy="44" r="2.6"/><circle cx="196" cy="38" r="2.6"/><circle cx="226" cy="28" r="2.6"/></g>
    <g text-anchor="middle"><text x="16" y="19">55</text><text x="46" y="15">58</text><text x="76" y="23">52</text><text x="106" y="13">59</text><text x="136" y="21">53</text><text x="166" y="15">57</text><text x="196" y="19">55</text><text x="226" y="7">63</text>
    <text x="16" y="56">30</text><text x="46" y="44">37</text><text x="76" y="56">30</text><text x="106" y="42">38</text><text x="136" y="52">32</text><text x="166" y="38">40</text><text x="196" y="32">45</text><text x="226" y="22">52</text>
    <text x="16" y="92">Text</text><text x="46" y="92">Text</text><text x="76" y="92">Text</text><text x="106" y="92">Text</text><text x="136" y="92">Text</text><text x="166" y="92">Text</text><text x="196" y="92">Text</text><text x="226" y="92">Text</text></g>
    <line x1="216" y1="97" x2="226" y2="97" stroke="var(--navy)" stroke-width="1.4"/><text x="229" y="99">Text</text>
    <line x1="216" y1="105" x2="226" y2="105" stroke="var(--green)" stroke-width="1.4"/><text x="229" y="107">Text</text>
  </svg>
  <div class="caption" style="left:34px;top:236px;width:280px"><b>Lorem ipsum</b>Lorem ipsum dolor sit amet, consetetur sadipscing elitr, sed diam nonumy eirmod tempor invidunt ut labore et dolore</div>
  <ul class="bullets" style="left:356px;top:66px;width:150px">
    <li>Lorem ipsum dolor sit amet, consetetur sadipscing elitr, sed diam nonumy eirmod tempor invidunt ut labore et dolore magna aliquyam erat, sed diam voluptua. At vero eos et accusam</li>
    <li>Lorem ipsum dolor sit amet, consetetur sadipscing elitr, sed diam nonumy eirmod tempor invidunt ut labore et dolore magna aliquyam erat, sed diam voluptua. At vero eos et accusam</li>
    <li>Lorem ipsum dolor sit amet, consetetur sadipscing elitr, sed diam nonumy eirmod tempor invidunt ut labore et dolore magna aliquyam erat, sed diam voluptua. At vero eos et accusam</li>
  </ul>
  <span class="page-no">13</span>
  <div class="bar-bottom"></div>
</section>

<section class="slide col-r" style="top:1952px">
  <div class="bar-top"></div>
  <h2 class="title">LOREM IPSUM DOLOR SIT AMET CONSETETUR</h2>
  <div class="caption" style="left:34px;top:46px;width:300px"><b style="font-size:7px">Lorem ipsum</b></div>
  <svg class="chart" style="left:22px;top:62px" width="310" height="80" viewBox="0 0 310 80">
    <g stroke="#ececec" stroke-width=".6"><line x1="16" y1="66" x2="308" y2="66"/><line x1="16" y1="50" x2="308" y2="50"/><line x1="16" y1="34" x2="308" y2="34"/><line x1="16" y1="18" x2="308" y2="18"/><line x1="16" y1="2" x2="308" y2="2"/></g>
    <g text-anchor="end"><text x="12" y="68">0</text><text x="12" y="52">20</text><text x="12" y="36">40</text><text x="12" y="20">60</text><text x="12" y="4">80</text></g>
    <polyline fill="none" stroke="var(--green)" stroke-width="1.4" points="28,44 52,40 76,30 100,18 124,24 148,28 172,30 196,34 220,32 244,38 268,36 292,30"/>
    <g fill="var(--green)"><circle cx="28" cy="44" r="1.6"/><circle cx="52" cy="40" r="1.6"/><circle cx="76" cy="30" r="1.6"/><circle cx="100" cy="18" r="1.6"/><circle cx="124" cy="24" r="1.6"/><circle cx="148" cy="28" r="1.6"/><circle cx="172" cy="30" r="1.6"/><circle cx="196" cy="34" r="1.6"/><circle cx="220" cy="32" r="1.6"/><circle cx="244" cy="38" r="1.6"/><circle cx="268" cy="36" r="1.6"/><circle cx="292" cy="30" r="1.6"/></g>
    <g text-anchor="middle" font-size="4"><text x="28" y="75">Jan</text><text x="52" y="75">Feb</text><text x="76" y="75">Mar</text><text x="100" y="75">Apr</text><text x="124" y="75">May</text><text x="148" y="75">Jun</text><text x="172" y="75">Jul</text><text x="196" y="75">Aug</text><text x="220" y="75">Sep</text><text x="244" y="75">Oct</text><text x="268" y="75">Nov</text><text x="292" y="75">Dec</text></g>
  </svg>
  <div class="caption" style="left:34px;top:146px;width:300px"><b style="font-size:7px">Lorem ipsum</b></div>
  <svg class="chart" style="left:22px;top:160px" width="310" height="80" viewBox="0 0 310 80">
    <g stroke="#ececec" stroke-width=".6"><line x1="16" y1="66" x2="308" y2="66"/><line x1="16" y1="50" x2="308" y2="50"/><line x1="16" y1="34" x2="308" y2="34"/><line x1="16" y1="18" x2="308" y2="18"/><line x1="16" y1="2" x2="308" y2="2"/></g>
    <g text-anchor="end"><text x="12" y="68">0</text><text x="12" y="52">20</text><text x="12" y="36">40</text><text x="12" y="20">60</text><text x="12" y="4">80</text></g>
    <g fill="var(--green)"><rect x="20" y="22" width="16" height="44"/><rect x="44" y="14" width="16" height="52"/><rect x="68" y="20" width="16" height="46"/><rect x="92" y="28" width="16" height="38"/><rect x="116" y="18" width="16" height="48"/><rect x="140" y="24" width="16" height="42"/><rect x="164" y="30" width="16" height="36"/><rect x="188" y="26" width="16" height="40"/><rect x="212" y="34" width="16" height="32"/><rect x="236" y="22" width="16" height="44"/><rect x="260" y="28" width="16" height="38"/><rect x="284" y="36" width="16" height="30"/></g>
    <g text-anchor="middle" font-size="4"><text x="28" y="75">Jan</text><text x="52" y="75">Feb</text><text x="76" y="75">Mar</text><text x="100" y="75">Apr</text><text x="124" y="75">May</text><text x="148" y="75">Jun</text><text x="172" y="75">Jul</text><text x="196" y="75">Aug</text><text x="220" y="75">Sep</text><text x="244" y="75">Oct</text><text x="268" y="75">Nov</text><text x="292" y="75">Dec</text></g>
  </svg>
  <ul class="bullets" style="left:356px;top:66px;width:150px">
    <li>Lorem ipsum dolor sit amet, consetetur sadipscing elitr, sed diam nonumy eirmod tempor invidunt ut labore et dolore magna aliquyam erat, sed diam voluptua. At vero eos et accusam</li>
    <li>Lorem ipsum dolor sit amet, consetetur sadipscing elitr, sed diam nonumy eirmod tempor invidunt ut labore et dolore magna aliquyam erat, sed diam voluptua. At vero eos et accusam</li>
    <li>Lorem ipsum dolor sit amet, consetetur sadipscing elitr, sed diam nonumy eirmod tempor invidunt ut labore et dolore magna aliquyam erat, sed diam voluptua. At vero eos et accusam</li>
  </ul>
  <span class="page-no">14</span>
  <div class="bar-bottom"></div>
</section>

<!-- Row 8 -->
<section class="slide col-l" style="top:2274px">
  <div class="bar-top"></div>
  <h2 class="title">LOREM IPSUM DOLOR SIT AMET CONSETETUR</h2>
  <div class="caption" style="left:34px;top:48px;width:300px"><b style="font-size:7px;margin-bottom:1px">Lorem ipsum</b><span style="font-size:5px">Lorem ipsum dolor sit amet, consetetur sadipscing elitr, sed diam nonumy eirmod</span></div>
  <svg class="chart" style="left:22px;top:70px" width="320" height="84" viewBox="0 0 320 84">
    <g stroke="#ececec" stroke-width=".6"><line x1="16" y1="70" x2="318" y2="70"/><line x1="16" y1="56" x2="318" y2="56"/><line x1="16" y1="42" x2="318" y2="42"/><line x1="16" y1="28" x2="318" y2="28"/><line x1="16" y1="14" x2="318" y2="14"/></g>
    <g text-anchor="end"><text x="12" y="72">0</text><text x="12" y="58">20</text><text x="12" y="44">40</text><text x="12" y="30">60</text><text x="12" y="16">80</text></g>
    <g fill="var(--green-dark)"><rect x="22" y="50" width="14" height="20"/><rect x="46" y="46" width="14" height="24"/><rect x="70" y="42" width="14" height="28"/><rect x="94" y="36" width="14" height="34"/><rect x="118" y="46" width="14" height="24"/><rect x="142" y="42" width="14" height="28"/><rect x="166" y="48" width="14" height="22"/><rect x="190" y="44" width="14" height="26"/><rect x="214" y="40" width="14" height="30"/><rect x="238" y="46" width="14" height="24"/><rect x="262" y="42" width="14" height="28"/><rect x="286" y="48" width="14" height="22"/></g>
    <g fill="var(--green)"><rect x="22" y="36" width="14" height="14"/><rect x="46" y="30" width="14" height="16"/><rect x="70" y="30" width="14" height="12"/><rect x="94" y="12" width="14" height="24"/><rect x="118" y="32" width="14" height="14"/><rect x="142" y="22" width="14" height="20"/><rect x="166" y="32" width="14" height="16"/><rect x="190" y="26" width="14" height="18"/><rect x="214" y="18" width="14" height="22"/><rect x="238" y="30" width="14" height="16"/><rect x="262" y="26" width="14" height="16"/><rect x="286" y="34" width="14" height="14"/></g>
    <g text-anchor="middle" font-size="4"><text x="29" y="79">Jan</text><text x="53" y="79">Feb</text><text x="77" y="79">Mar</text><text x="101" y="79">Apr</text><text x="125" y="79">May</text><text x="149" y="79">Jun</text><text x="173" y="79">Jul</text><text x="197" y="79">Aug</text><text x="221" y="79">Sep</text><text x="245" y="79">Oct</text><text x="269" y="79">Nov</text><text x="293" y="79">Dec</text></g>
  </svg>
  <div class="caption" style="left:34px;top:156px;width:300px"><b style="font-size:7px;margin-bottom:1px">Lorem ipsum</b><span style="font-size:5px">Lorem ipsum dolor sit amet, consetetur sadipscing elitr, sed diam nonumy eirmod</span></div>
  <svg class="chart" style="left:22px;top:178px" width="320" height="84" viewBox="0 0 320 84">
    <g stroke="#ececec" stroke-width=".6"><line x1="16" y1="70" x2="318" y2="70"/><line x1="16" y1="56" x2="318" y2="56"/><line x1="16" y1="42" x2="318" y2="42"/><line x1="16" y1="28" x2="318" y2="28"/><line x1="16" y1="14" x2="318" y2="14"/></g>
    <g text-anchor="end"><text x="12" y="72">0</text><text x="12" y="58">20</text><text x="12" y="44">40</text><text x="12" y="30">60</text><text x="12" y="16">80</text></g>
    <g fill="var(--green-dark)"><rect x="22" y="50" width="14" height="20"/><rect x="46" y="44" width="14" height="26"/><rect x="70" y="46" width="14" height="24"/><rect x="94" y="40" width="14" height="30"/><rect x="118" y="44" width="14" height="26"/><rect x="142" y="48" width="14" height="22"/><rect x="166" y="42" width="14" height="28"/><rect x="190" y="38" width="14" height="32"/><rect x="214" y="44" width="14" height="26"/><rect x="238" y="40" width="14" height="30"/><rect x="262" y="46" width="14" height="24"/><rect x="286" y="42" width="14" height="28"/></g>
    <g fill="var(--green)"><rect x="22" y="36" width="14" height="14"/><rect x="46" y="32" width="14" height="12"/><rect x="70" y="30" width="14" height="16"/><rect x="94" y="24" width="14" height="16"/><rect x="118" y="30" width="14" height="14"/><rect x="142" y="34" width="14" height="14"/><rect x="166" y="22" width="14" height="20"/><rect x="190" y="16" width="14" height="22"/><rect x="214" y="26" width="14" height="18"/><rect x="238" y="18" width="14" height="22"/><rect x="262" y="30" width="14" height="16"/><rect x="286" y="24" width="14" height="18"/></g>
    <g text-anchor="middle" font-size="4"><text x="29" y="79">Jan</text><text x="53" y="79">Feb</text><text x="77" y="79">Mar</text><text x="101" y="79">Apr</text><text x="125" y="79">May</text><text x="149" y="79">Jun</text><text x="173" y="79">Jul</text><text x="197" y="79">Aug</text><text x="221" y="79">Sep</text><text x="245" y="79">Oct</text><text x="269" y="79">Nov</text><text x="293" y="79">Dec</text></g>
  </svg>
  <p class="note" style="left:356px;top:72px;width:150px">Lorem ipsum dolor sit amet, consetetur sadipscing elitr, sed diam nonumy eirmod tempor invidunt ut labore et dolore magna aliquyam erat, sed diam voluptua. At vero eos et accusam</p>
  <p class="note" style="left:356px;top:180px;width:150px">Lorem ipsum dolor sit amet, consetetur sadipscing elitr, sed diam nonumy eirmod tempor invidunt ut labore et dolore magna aliquyam erat, sed diam voluptua. At vero eos et accusam</p>
  <span class="page-no">15</span>
  <div class="bar-bottom"></div>
</section>

<section class="slide col-r" style="top:2274px">
  <div class="bar-top"></div>
  <h2 class="title">LOREM IPSUM DOLOR SIT AMET CONSETETUR</h2>
  <div class="caption" style="left:34px;top:44px;width:320px"><b style="font-size:7px;margin-bottom:1px">Lorem ipsum</b><span style="font-size:5px">Lorem ipsum dolor sit amet, consetetur sadipscing elitr, sed diam nonumy eirmod tempor invidunt ut labore et dolore magna aliquyam erat, sed diam voluptua. At vero eos et accusam et justo duo dolores</span></div>
  <svg class="chart" style="left:34px;top:80px" width="310" height="190" viewBox="0 0 310 190">
    <g font-size="6"><text x="0" y="9">Text</text><text x="0" y="26">Text</text><text x="0" y="43">Text</text><text x="0" y="60">Text</text><text x="0" y="77">Text</text><text x="0" y="94">Text</text><text x="0" y="111">Text</text><text x="0" y="128">Text</text><text x="0" y="145">Text</text><text x="0" y="162">Text</text></g>
    <g fill="var(--green-dark)"><rect x="22" y="2" width="186" height="10"/><rect x="22" y="19" width="172" height="10"/><rect x="22" y="36" width="154" height="10"/><rect x="22" y="53" width="142" height="10"/><rect x="22" y="70" width="166" height="10"/><rect x="22" y="87" width="130" height="10"/><rect x="22" y="104" width="124" height="10"/><rect x="22" y="121" width="100" height="10"/><rect x="22" y="138" width="82" height="10"/><rect x="22" y="155" width="76" height="10"/></g>
    <g fill="#333" font-size="6"><text x="212" y="10">31</text><text x="198" y="27">29</text><text x="180" y="44">26</text><text x="168" y="61">24</text><text x="192" y="78">28</text><text x="156" y="95">22</text><text x="150" y="112">21</text><text x="126" y="129">17</text><text x="108" y="146">14</text><text x="102" y="163">13</text></g>
    <line x1="270" y1="0" x2="270" y2="168" stroke="#bbb" stroke-width=".6"/>
    <g fill="var(--green)"><rect x="270" y="3" width="14" height="7"/><rect x="270" y="20" width="24" height="7"/><rect x="260" y="37" width="10" height="7"/><rect x="270" y="54" width="8" height="7"/><rect x="270" y="71" width="18" height="7"/><rect x="270" y="88" width="12" height="7"/><rect x="270" y="105" width="6" height="7"/><rect x="264" y="122" width="6" height="7"/><rect x="270" y="139" width="26" height="7"/><rect x="270" y="156" width="10" height="7"/></g>
    <g font-size="4.5"><text x="287" y="9">+7%</text><text x="297" y="26">+14%</text><text x="244" y="43">-5%</text><text x="281" y="60">+4%</text><text x="291" y="77">+10%</text><text x="285" y="94">+6%</text><text x="279" y="111">+3%</text><text x="250" y="128">-3%</text><text x="298" y="145">+16%</text><text x="283" y="162">+5%</text></g>
  </svg>
  <ul class="bullets" style="left:356px;top:66px;width:150px">
    <li>Lorem ipsum dolor sit amet, consetetur sadipscing elitr, sed diam nonumy eirmod tempor invidunt ut labore et dolore magna aliquyam erat, sed diam voluptua. At vero eos et accusam</li>
    <li>Lorem ipsum dolor sit amet, consetetur sadipscing elitr, sed diam nonumy eirmod tempor invidunt ut labore et dolore magna aliquyam erat, sed diam voluptua. At vero eos et accusam</li>
    <li>Lorem ipsum dolor sit amet, consetetur sadipscing elitr, sed diam nonumy eirmod tempor invidunt ut labore et dolore magna aliquyam erat, sed diam voluptua. At vero eos et accusam</li>
  </ul>
  <span class="page-no">16</span>
  <div class="bar-bottom"></div>
</section>

<!-- Row 9 -->
<section class="slide col-l" style="top:2596px">
  <div class="bar-top"></div>
  <h2 class="title">LOREM IPSUM DOLOR SIT AMET CONSETETUR</h2>
  <svg class="chart" style="left:30px;top:66px" width="210" height="60" viewBox="0 0 210 60">
    <g fill="none" stroke-width="9">
      <circle cx="30" cy="30" r="24" stroke="#e4e4e4"/><circle cx="30" cy="30" r="24" stroke="var(--green-mid)" stroke-dasharray="116.1 150.8" transform="rotate(-90 30 30)"/>
      <circle cx="102" cy="30" r="24" stroke="#e4e4e4"/><circle cx="102" cy="30" r="24" stroke="var(--green-mid)" stroke-dasharray="104.1 150.8" transform="rotate(-90 102 30)"/>
      <circle cx="174" cy="30" r="24" stroke="#e4e4e4"/><circle cx="174" cy="30" r="24" stroke="var(--green-mid)" stroke-dasharray="134.2 150.8" transform="rotate(-90 174 30)"/>
    </g>
  </svg>
  <div class="big-num" style="left:30px;top:140px">77%</div>
  <div class="big-num" style="left:102px;top:140px">69%</div>
  <div class="big-num" style="left:174px;top:140px">89%</div>
  <div class="caption" style="left:34px;top:196px;width:62px"><b style="font-size:7px">Lorem ipsum</b>Lorem ipsum dolor sit amet, consetetur sadipscing elitr, sed diam nonumy eirmod tempor</div>
  <div class="caption" style="left:106px;top:196px;width:62px"><b style="font-size:7px">Lorem ipsum</b>Lorem ipsum dolor sit amet, consetetur sadipscing elitr, sed diam nonumy eirmod tempor</div>
  <div class="caption" style="left:178px;top:196px;width:62px"><b style="font-size:7px">Lorem ipsum</b>Lorem ipsum dolor sit amet, consetetur sadipscing elitr, sed diam nonumy eirmod tempor</div>
  <div class="caption" style="left:300px;top:60px;width:210px;text-align:center"><b style="font-size:7px;margin-bottom:1px">Lorem ipsum</b><span style="font-size:5px">Lorem ipsum dolor sit amet, consetetur sadipscing elitr, sed diam nonumy eirmod tempor</span></div>
  <svg class="chart" style="left:300px;top:96px" width="210" height="174" viewBox="0 0 210 174">
    <line x1="0" y1="170" x2="210" y2="170" stroke="#ccc" stroke-width=".6"/>
    <rect x="6" y="134" width="36" height="36" fill="var(--green)"/>
    <rect x="46" y="112" width="36" height="58" fill="var(--green-mid)"/>
    <rect x="86" y="52" width="36" height="118" fill="var(--green-mid)"/>
    <rect x="126" y="24" width="36" height="146" fill="var(--green-dark)"/>
    <rect x="166" y="94" width="36" height="76" fill="var(--green-mid)"/>
    <g fill="#fff" font-size="7" text-anchor="middle"><text x="24" y="146">Text</text><text x="24" y="157">17</text><text x="64" y="124">Text</text><text x="64" y="135">26</text><text x="104" y="64">Text</text><text x="104" y="75">53</text><text x="144" y="36">Text</text><text x="144" y="47">66</text><text x="184" y="106">Text</text><text x="184" y="117">34</text></g>
  </svg>
  <span class="page-no">17</span>
  <div class="bar-bottom"></div>
</section>

<section class="slide col-r" style="top:2596px">
  <div class="bar-top"></div>
  <h2 class="title">LOREM IPSUM DOLOR SIT AMET CONSETETUR</h2>
  <svg class="chart" style="left:34px;top:56px" width="240" height="112" viewBox="0 0 240 112">
    <line x1="0" y1="110" x2="240" y2="110" stroke="#ccc" stroke-width=".6"/>
    <rect x="4" y="60" width="32" height="50" fill="var(--green)"/><rect x="38" y="40" width="32" height="70" fill="var(--green-mid)"/>
    <rect x="84" y="50" width="32" height="60" fill="var(--green)"/><rect x="118" y="20" width="32" height="90" fill="var(--green-mid)"/>
    <rect x="164" y="44" width="32" height="66" fill="var(--green)"/><rect x="198" y="6" width="32" height="104" fill="var(--green-mid)"/>
    <g fill="#fff" font-size="6.5" text-anchor="middle"><text x="20" y="72">Text</text><text x="20" y="82">17</text><text x="54" y="52">Text</text><text x="54" y="62">26</text><text x="100" y="62">Text</text><text x="100" y="72">22</text><text x="134" y="32">Text</text><text x="134" y="42">35</text><text x="180" y="56">Text</text><text x="180" y="66">24</text><text x="214" y="18">Text</text><text x="214" y="28">54</text></g>
  </svg>
  <div class="big-num" style="left:42px;top:176px;width:70px">+9</div>
  <div class="big-num" style="left:122px;top:176px;width:70px">+13</div>
  <div class="big-num" style="left:202px;top:176px;width:70px">+30</div>
  <div class="caption" style="left:38px;top:212px;width:72px"><b style="font-size:7px">Lorem ipsum</b>Lorem ipsum dolor sit amet, consetetur sadipscing elitr, sed diam nonumy eirmod tempor</div>
  <div class="caption" style="left:118px;top:212px;width:72px"><b style="font-size:7px">Lorem ipsum</b>Lorem ipsum dolor sit amet, consetetur sadipscing elitr, sed diam nonumy eirmod tempor</div>
  <div class="caption" style="left:198px;top:212px;width:72px"><b style="font-size:7px">Lorem ipsum</b>Lorem ipsum dolor sit amet, consetetur sadipscing elitr, sed diam nonumy eirmod tempor</div>
  <div class="caption" style="left:340px;top:58px;width:170px"><b style="font-size:7.5px;margin-bottom:1px">Lorem ipsum</b><span style="font-size:5px">Lorem ipsum dolor sit amet, consetetur sadipscing elitr, sed diam</span></div>
  <svg class="chart" style="left:356px;top:100px" width="140" height="140" viewBox="0 0 140 140">
    <circle cx="70" cy="70" r="56" fill="none" stroke="#e4e4e4" stroke-width="16"/>
    <circle cx="70" cy="70" r="56" fill="none" stroke="var(--green-mid)" stroke-width="16" stroke-dasharray="270.9 351.9" transform="rotate(-90 70 70)"/>
    <text x="70" y="58" text-anchor="middle" style="font-size:8px;fill:#888">Text</text>
    <text x="70" y="84" text-anchor="middle" style="font-size:26px;fill:var(--green-mid);font-family:'Libre Franklin',Arial,sans-serif">77%</text>
  </svg>
  <span class="page-no">18</span>
  <div class="bar-bottom"></div>
</section>

</body>
</html>
```